Design some Business Cards for Consultant

Most of my work is in financial & analytical consulting for microfinance and low-income housing finance, mainly in developing countries (Asia, Africa, Latin America). You can see samples of my published work here: tobiaswenkle.com (main page is the blog; navigate to /papers for other published work).

Looking for a clean, no-nonsense design with limited text (name, city, website, email, skype & phone). Single-sided. Would like to print on recycled paper stock, so consider this in the design. If you can work with a (reasonably priced) online printer that ships to Belgium at reasonable cost, would pay extra for the reference and selection of appropriate paper stock, but this isn't required.

Don't hesitate if you need additional info for your design. Will provide detailed text to the contest winner.

```html
<!DOCTYPE html>
<html lang="en">
<head>
<meta charset="utf-8">
<title>Tobias Wenkle – Business Card</title>
<link rel="stylesheet" href="https://fonts.googleapis.com/css2?family=Open+Sans:wght@400;600;700&display=swap">
<style>
  :root {
    --backdrop: #3b3837;
    --paper: #ebebe9;
    --paper-edge: #e2e2df;
    --ink: #3f3f3f;
    --ink-soft: #4a4a4a;
  }
  html, body {
    margin: 0;
    padding: 0;
    width: 1200px;
    height: 969px;
    overflow: hidden;
    background: var(--backdrop);
    font-family: "Open Sans", sans-serif;
  }
  .card {
    position: absolute;
    left: 80px;
    top: 197px;
    width: 1040px;
    height: 574px;
    border-radius: 18px;
    background: radial-gradient(ellipse at 40% 35%, var(--paper) 0%, var(--paper-edge) 100%);
    color: var(--ink);
  }
  .card > * { position: absolute; margin: 0; line-height: 1; white-space: nowrap; }
  .name {
    left: 88px; top: 67px;
    font-size: 34px; font-weight: 700; color: var(--ink);
  }
  .role {
    left: 88px; top: 103px;
    font-size: 26px; font-weight: 400; color: var(--ink-soft);
  }
  .address {
    left: 88px; top: 222px;
    font-size: 21px; line-height: 29px; color: var(--ink-soft);
  }
  .contacts {
    left: 88px; top: 316px;
    list-style: none; padding: 0;
    font-size: 21px; color: var(--ink-soft);
  }
  .contacts li {
    display: flex; align-items: center;
    height: 36px;
  }
  .contacts svg {
    width: 28px; height: 28px;
    margin-right: 16px;
    fill: none; stroke: var(--ink); stroke-width: 2.2;
  }
  .contacts .solid { fill: var(--ink); stroke: none; }
  .website {
    left: 88px; top: 496px;
    font-size: 24px; letter-spacing: 4px; color: var(--ink);
  }
  .website strong { font-weight: 600; }
</style>
</head>
<body>
  <div class="card">
    <h1 class="name">Tobias Wenkle, Ledgerline</h1>
    <p class="role">Director</p>
    <p class="address">Level 2, 148 - 150 Marlowe Street,<br>Fenwick VIC 3071 Australia</p>
    <ul class="contacts">
      <li>
        <svg viewBox="0 0 28 28" aria-hidden="true">
          <path class="solid" d="M4 11c0-3 4-5 10-5s10 2 10 5v2h-5v-3H9v3H4z"/>
          <rect class="solid" x="6" y="14" width="16" height="9" rx="2"/>
        </svg>
        1 234 567 890
      </li>
      <li>
        <svg viewBox="0 0 28 28" aria-hidden="true">
          <rect x="8" y="3" width="12" height="22" rx="2.5"/>
          <line x1="12" y1="21" x2="16" y2="21"/>
        </svg>
        1 234 567 890
      </li>
      <li>
        <svg viewBox="0 0 28 28" aria-hidden="true">
          <rect x="3" y="7" width="22" height="15" rx="1.5"/>
          <path d="M3 8l11 8 11-8"/>
        </svg>
        tobias@tobiaswenkle.com
      </li>
      <li>
        <svg viewBox="0 0 28 28" aria-hidden="true">
          <path d="M5 6h18a2 2 0 0 1 2 2v10a2 2 0 0 1-2 2H12l-5 4v-4H5a2 2 0 0 1-2-2V8a2 2 0 0 1 2-2z"/>
        </svg>
        your handle
      </li>
    </ul>
    <p class="website">www.<strong>tobiaswenkle</strong>.com</p>
  </div>
</body>
</html>
```